Bold Cover needed for a book on Workplace Bullying

I need a book cover design for a book titled, “Iron Silence?” The book recounts my story of bullying in the workplace. It also includes chapters on how readers can minimize/stop workplace bullying, write an effective complaint, and ensure their own mental wellbeing.
I am looking for a bold design using red and black, and possibly distressed lettering. The covers of other books dealing with this subject do not reflect my vision. They are often too childish or look too academic. This book needs to stress the serious nature of a toxic workplace, while appealing to readers experiencing a similar situation. I’d like the cover to reflect the mental anguish associated with workplace bullying (hence the distressed lettering).
I have included a cover that appeals to me (although the coloring is wrong). That said, I am also very happy (and excited) to see your creative input!
On the cover, it should have the following:
Title: Iron Silence?
Subtitle: How the Harbour Works Department Condones Bullying & Ruins Lives
Author: Owen Frick
Other relevant details:
Book size: 5.5” x 8.5”
Back cover will have a blurb, author picture/short bio, and barcode
The blurb on the back cover reads:
Undermining, intimidation and threats
Despite the Department of Harbour Works allegedly holding a zero tolerance for bullying, these behaviours were an everyday occurrence in at least one workplace. Even after a decade of complaints, numerous witnesses and physical proof, the department failed to act. Instead, they looked the other way, allowing one powerful and well-connected individual to end careers and ruin lives.
After being targeted, one teacher resolved to put an end to the abuse experienced by more than fifty employees. His startling story reveals the relentless bullying, mental health ramifications, and insidious tactics used to cover up the corrosive behaviour.
Those who have experienced a toxic workplace will also find much needed support and guidance, intended to minimise suffering and detail a clear way forward. Chapters include dealing with bullying in the workplace, how to lodge a successful complaint, and how to stay sane during any potential legal action.

```html
<!DOCTYPE html>
<html lang="en">
<head>
<meta charset="utf-8">
<title>Iron Silence? — Owen Frick</title>
<link rel="stylesheet" href="https://fonts.googleapis.com/css2?family=Cinzel:wght@600;700&family=Marcellus&family=Josefin+Sans:wght@600&display=swap">
<style>
  :root {
    --page: #ffffff;
    --title-red: #c4161c;
    --ink: #141211;
    --cream: #efe6d8;
    --subtitle: #f6efe4;
    --art-red: #b8252a;
    --art-blush: #e9c7b8;
    --art-sepia: #8c8278;
    --art-dark: #1b1816;
  }
  * { box-sizing: border-box; margin: 0; padding: 0; }
  html, body {
    width: 1200px;
    height: 1106px;
    overflow: hidden;
    background: var(--page);
  }
  .canvas {
    position: relative;
    width: 1200px;
    height: 1106px;
  }
  .book-cover {
    position: absolute;
    left: 276px;
    top: 53px;
    width: 647px;
    height: 1000px;
    overflow: hidden;
  }
  .cover-art {
    position: absolute;
    inset: 0;
    background:
      radial-gradient(ellipse 70% 22% at 50% 28%, rgba(250,236,224,0.92), rgba(250,236,224,0) 70%),
      linear-gradient(180deg,
        var(--art-red) 0%,
        #d98f84 12%,
        var(--art-blush) 24%,
        #e6b9ab 36%,
        #c9685f 48%,
        var(--art-sepia) 62%,
        #6b625a 76%,
        #3a3430 86%,
        var(--art-dark) 100%);
  }
  .cover-text {
    position: absolute;
    inset: 0;
    text-align: center;
  }
  .title-main {
    position: absolute;
    top: 130px;
    left: 0;
    right: 0;
    font-family: "Cinzel", serif;
    font-weight: 700;
    font-size: 176px;
    line-height: 1;
    letter-spacing: 2px;
    color: var(--title-red);
    text-shadow: 2px 3px 0 rgba(60,0,0,0.35);
  }
  .title-sub {
    position: absolute;
    top: 310px;
    left: 0;
    right: 0;
    font-family: "Marcellus", serif;
    font-size: 62px;
    line-height: 1;
    letter-spacing: 1px;
    color: var(--ink);
  }
  .subtitle {
    position: absolute;
    top: 798px;
    left: 30px;
    right: 30px;
    font-family: "Josefin Sans", sans-serif;
    font-weight: 600;
    font-size: 23px;
    line-height: 1.2;
    letter-spacing: 1px;
    text-transform: uppercase;
    color: var(--subtitle);
  }
  .author {
    position: absolute;
    top: 905px;
    left: 0;
    right: 0;
    font-family: "Marcellus", serif;
    font-size: 64px;
    line-height: 1;
    letter-spacing: 2px;
    text-transform: uppercase;
    color: var(--cream);
  }
</style>
</head>
<body>
  <div class="canvas">
    <div class="book-cover">
      <div class="cover-art" role="img" aria-label="Vintage sepia and red illustration of a distressed woman holding her head, surrounded by men in suits leaning over a table, with grotesque red faces looming above"></div>
      <div class="cover-text">
        <h1 class="title-main">IRON</h1>
        <p class="title-sub">SILENCE?</p>
        <p class="subtitle">How the Harbour Works Department<br>Condones Bullying &amp; Ruins Lives</p>
        <p class="author">Owen Frick</p>
      </div>
    </div>
  </div>
</body>
</html>
```